Veterinary Business cards

Redesign Business Card

Information needed on Card:
Hours: Mon-Fri: 4pm -10PM; Sat- Sun- 10 AM- 5PM
Help@bayfernvet.com
www.bayfernvet.com
555-718-2946
4173 SE 19th Ave. okc, ok 73958
*No appointment necessary*

Optional:
Our tag line is "We're here when you need us" - If it fits on the cards.

```html
<!DOCTYPE html>
<html lang="en">
<head>
<meta charset="utf-8">
<title>Bayfern Urgent Care – Business Card</title>
<link rel="stylesheet" href="https://fonts.googleapis.com/css2?family=Montserrat:wght@400;500;700&family=Crimson+Pro:wght@700&family=Lora:wght@400&display=swap">
<style>
  :root {
    --navy: #031f6e;
    --orange: #d96200;
    --ink: #111111;
    --paper: #ffffff;
    --backdrop: #e6e6e6;
  }
  * { margin: 0; padding: 0; box-sizing: border-box; }
  html, body { width: 1048px; height: 1200px; overflow: hidden; background: var(--backdrop); }
  .canvas { position: relative; width: 1048px; height: 1200px; font-family: "Montserrat", sans-serif; }

  .card { position: absolute; width: 843px; height: 481px; box-shadow: 0 6px 22px rgba(0,0,0,0.28); overflow: hidden; }
  .card-front { left: 84px; top: 87px; background: var(--paper); }
  .card-back { left: 80px; top: 622px; background: var(--navy); }

  .brand { position: absolute; display: flex; align-items: center; gap: 14px; font-family: "Montserrat", sans-serif; font-weight: 500; }
  .brand-dot { width: 22px; height: 22px; border-radius: 50%; flex: none; }
  .brand-name { line-height: 1.15; letter-spacing: 2px; }
  .brand-front { left: 468px; top: 118px; color: var(--navy); }
  .brand-front .brand-dot { background: var(--orange); }
  .brand-front .brand-name { font-size: 36px; }
  .brand-back { left: 0; right: 0; top: 150px; justify-content: center; color: var(--paper); gap: 20px; }
  .brand-back .brand-dot { background: var(--orange); width: 34px; height: 34px; }
  .brand-back .brand-name { font-size: 62px; }

  .person-name { position: absolute; left: 36px; top: 218px; font-family: "Crimson Pro", serif; font-weight: 700; font-size: 40px; color: var(--navy); letter-spacing: -1.2px; line-height: 1; }
  .person-title { position: absolute; left: 36px; top: 261px; font-size: 23px; color: var(--ink); letter-spacing: 0.4px; }
  .divider { position: absolute; left: 36px; width: 770px; top: 298px; height: 2px; background: var(--ink); }

  .contact-list { position: absolute; left: 36px; top: 318px; list-style: none; }
  .contact-list li { display: flex; align-items: center; height: 34.5px; font-size: 23px; color: var(--ink); letter-spacing: 0.3px; }
  .contact-list svg { width: 20px; height: 20px; margin-right: 20px; flex: none; }

  .visit-info { position: absolute; right: 37px; top: 322px; text-align: right; color: var(--ink); }
  .walk-in { font-weight: 700; font-size: 23px; letter-spacing: 0.2px; }
  .address { font-size: 22px; margin-top: 12px; letter-spacing: 0.2px; }

  .rule-navy { position: absolute; left: 0; right: 0; top: 425px; height: 3px; background: var(--navy); }
  .hours-band { position: absolute; left: 0; right: 0; top: 433px; height: 48px; background: var(--orange); color: var(--paper); font-weight: 700; font-size: 25px; display: flex; align-items: center; justify-content: center; letter-spacing: 0.3px; }

  .tagline { position: absolute; left: 0; right: 0; top: 400px; text-align: center; font-family: "Lora", serif; font-size: 27px; color: var(--paper); }
</style>
</head>
<body>
<div class="canvas">

  <section class="card card-front">
    <div class="brand brand-front">
      <span class="brand-dot"></span>
      <span class="brand-name">BAYFERN<br>URGENT CARE</span>
    </div>

    <h1 class="person-name">MARCUS DELANE</h1>
    <p class="person-title">Managing Director</p>
    <div class="divider"></div>

    <ul class="contact-list">
      <li>
        <svg viewBox="0 0 24 24" aria-hidden="true"><path fill="var(--orange)" d="M6.6 10.8a15.1 15.1 0 0 0 6.6 6.6l2.2-2.2c.3-.3.7-.4 1-.2 1.1.4 2.3.6 3.6.6.6 0 1 .4 1 1V20c0 .6-.4 1-1 1A17 17 0 0 1 3 4c0-.6.4-1 1-1h3.5c.6 0 1 .4 1 1 0 1.3.2 2.5.6 3.6.1.3 0 .7-.2 1z"/></svg>
        555-718-2946
      </li>
      <li>
        <svg viewBox="0 0 24 24" aria-hidden="true"><rect x="2" y="5" width="20" height="14" fill="var(--orange)"/><path d="M2 5l10 8 10-8" fill="none" stroke="#fff" stroke-width="1.6"/></svg>
        Help@bayfernvet.com
      </li>
      <li>
        <svg viewBox="0 0 24 24" aria-hidden="true"><circle cx="12" cy="12" r="10" fill="var(--orange)"/><path d="M2 12h20M12 2c3 3 3 17 0 20M12 2c-3 3-3 17 0 20" fill="none" stroke="#fff" stroke-width="1.4"/></svg>
        www.bayfernvet.com
      </li>
    </ul>

    <div class="visit-info">
      <p class="walk-in">*No appointment necessary*</p>
      <p class="address">4173 SE 19th Ave. okc, ok 73958</p>
    </div>

    <div class="rule-navy"></div>
    <div class="hours-band">Hours: Mon-Fri: 4pm -10PM; Sat- Sun- 10 AM- 5PM</div>
  </section>

  <section class="card card-back">
    <div class="brand brand-back">
      <span class="brand-dot"></span>
      <span class="brand-name">BAYFERN</span>
    </div>
    <p class="tagline">We're here when you need us</p>
  </section>

</div>
</body>
</html>
```